Business is backhoe and truck hire. As the title indicates, we dig dirt. Colours preferred are charcoal, red and or orange. Would like a backhoe on the card,possibly a designs with the silhouette of the machine in the background. I We would like to incorporate a large tick in the title for solutions. I thought it could be part of the "W" . Our shirts are Black polo's with orange lines around sleeves and sides. We are a new business in rural Qld, happy to do the smaller jobs that others wont.

Industry/Entity Type

Business

Contact Information for Business Card

Tall Creek Groundworks Services

Backhoe and Truck Hire
ABN:81264950173

Peter Holloway
PH: 0491 732 580
PH: 0493 618 204
PH: 4683 1057 a/h

email: tcgservices@mailbox-example.net

```html
<!DOCTYPE html>
<html lang="en">
<head>
<meta charset="utf-8">
<title>Tall Creek Groundworks Services – Business Card</title>
<link rel="stylesheet" href="https://fonts.googleapis.com/css2?family=Arimo:wght@700&family=Stardos+Stencil:wght@700&display=swap">
<style>
  :root {
    --backdrop: #ececec;
    --sky-top: #e31e26;
    --sky-mid: #ef5a2c;
    --sky-bottom: #f8a43c;
    --charcoal: #2f2e2e;
    --machine: #1c1b1b;
    --ink: #363636;
    --white: #ffffff;
    --band-text: #ececec;
  }
  html, body {
    margin: 0;
    width: 1200px;
    height: 806px;
    overflow: hidden;
    background: var(--backdrop);
  }
  .card {
    position: absolute;
    left: 125px;
    top: 118px;
    width: 950px;
    height: 546px;
    overflow: hidden;
    background: linear-gradient(180deg, var(--sky-top) 0%, var(--sky-mid) 40%, var(--sky-bottom) 80%);
    font-family: "Arimo", Arial, sans-serif;
  }
  .company-name {
    position: absolute;
    right: 82px;
    top: 62px;
    margin: 0;
    font-size: 40px;
    font-weight: 700;
    color: var(--white);
    white-space: nowrap;
  }
  .abn {
    position: absolute;
    right: 82px;
    top: 116px;
    margin: 0;
    font-size: 23px;
    font-weight: 700;
    color: var(--white);
  }
  .contact {
    position: absolute;
    left: 475px;
    top: 190px;
    color: var(--ink);
    font-weight: 700;
  }
  .contact-name {
    margin: 0 0 0 44px;
    font-size: 28px;
  }
  .phone-block {
    position: relative;
    margin: 18px 0 0 46px;
    font-size: 25px;
    line-height: 31.5px;
  }
  .phone-icon {
    position: absolute;
    left: -40px;
    top: 38px;
    width: 22px;
    height: 26px;
  }
  .email-row {
    display: flex;
    align-items: center;
    margin-top: 4px;
    font-size: 24px;
  }
  .email-icon {
    width: 32px;
    height: 22px;
    margin-right: 14px;
  }
  .machine-area {
    position: absolute;
    left: 18px;
    top: 265px;
    width: 400px;
    height: 185px;
    background: var(--machine);
    border-radius: 10px 10px 0 0;
  }
  .ground-band {
    position: absolute;
    left: 0;
    top: 420px;
    width: 100%;
    height: 126px;
    background: var(--charcoal);
  }
  .service-line {
    position: absolute;
    left: 90px;
    top: 462px;
    margin: 0;
    font-family: "Stardos Stencil", "Courier New", monospace;
    font-size: 54px;
    font-weight: 700;
    letter-spacing: 4px;
    color: var(--band-text);
    white-space: nowrap;
  }
</style>
</head>
<body>
  <div class="card">
    <h1 class="company-name">Tall Creek Groundworks Services</h1>
    <p class="abn">ABN:81264950173</p>

    <div class="contact">
      <p class="contact-name">Peter Holloway</p>
      <div class="phone-block">
        <svg class="phone-icon" viewBox="0 0 22 26" aria-hidden="true">
          <path d="M6 1 L9 7 L6.5 9 C7.5 13 9.5 16.5 12.5 19 L15 17 L20 21 L17 25 C9 23 3 14 2 4 Z" fill="none" stroke="var(--ink)" stroke-width="2" stroke-linejoin="round"/>
        </svg>
        <div>0491 732 580</div>
        <div>0493 618 204</div>
        <div>4683 1057</div>
      </div>
      <div class="email-row">
        <svg class="email-icon" viewBox="0 0 32 22" aria-hidden="true">
          <rect x="1.5" y="1.5" width="29" height="19" fill="none" stroke="var(--ink)" stroke-width="2.5"/>
          <path d="M1.5 1.5 L16 12 L30.5 1.5" fill="none" stroke="var(--ink)" stroke-width="2.5"/>
        </svg>
        <span>tcgservices@mailbox-example.net</span>
      </div>
    </div>

    <div class="machine-area" role="img" aria-label="Silhouette of a backhoe loader with raised digging arm and front bucket"></div>
    <div class="ground-band"></div>
    <p class="service-line">BACKHOE AND TRUCK HIRE</p>
  </div>
</body>
</html>
```